Need Business Card for eLearning Company

Need a business card designed for our company, CareerPathlane.

CareerPathlane has developed a complete 12 lesson eLearning course to teach you the skills you need to present yourself in a job interview. The course uses advanced learning techniques in the multimedia videos, plus contains quizzes and additional exercises to insure you get the course and can walk into any interview with confidence and ease, and get the job.

www.careerpathlane-demo.com

Attached is our logo

Industry/Entity Type

Business

```html
<!DOCTYPE html>
<html lang="en">
<head>
<meta charset="utf-8">
<title>CareerPathlane Business Card</title>
<link rel="stylesheet" href="https://fonts.googleapis.com/css2?family=Questrial&display=swap">
<style>
  :root {
    --backdrop: #2a292a;
    --card-white: #ffffff;
    --card-dark: #3b393a;
    --ink: #4a4a4a;
    --ink-soft: #6b6b6b;
    --rule: #bdbdbd;
    --green: #8cb92b;
    --purple: #8a1f7a;
    --white: #ffffff;
  }
  * { box-sizing: border-box; margin: 0; padding: 0; }
  html, body {
    width: 1200px; height: 675px; overflow: hidden;
    background: var(--backdrop);
    font-family: "Questrial", "Century Gothic", sans-serif;
  }
  .stage {
    width: 1200px; height: 675px;
    display: flex; align-items: center; justify-content: center; gap: 40px;
  }
  .card {
    width: 540px; height: 309px; position: relative;
    box-shadow: 0 10px 30px rgba(0,0,0,.45);
  }
  .card--front { background: var(--card-white); color: var(--ink); }
  .card--back { background: var(--card-dark); color: var(--white); }

  .brand { position: absolute; display: flex; flex-direction: column; align-items: flex-start; }
  .brand__row { display: flex; align-items: center; gap: 10px; }
  .brand__dot { width: 18px; height: 18px; border-radius: 50%; }
  .brand__name { font-size: 30px; letter-spacing: .5px; line-height: 1; }
  .brand__tagline {
    font-size: 9px; letter-spacing: 1.4px; text-transform: uppercase;
    margin-left: 28px; margin-top: 3px;
  }
  .card--front .brand { left: 160px; top: 44px; }
  .card--front .brand__dot { background: var(--purple); }
  .card--front .brand__name { color: var(--ink); }
  .card--front .brand__tagline { color: var(--ink); }

  .card--back .brand { left: 50%; top: 108px; transform: translateX(-50%); }
  .card--back .brand__dot { background: var(--white); }
  .card--back .brand__name { color: var(--white); font-size: 34px; }
  .card--back .brand__tagline { color: var(--white); }
  .card--back .web {
    position: absolute; left: 0; right: 0; top: 190px;
    text-align: center; font-size: 13px; letter-spacing: .5px; font-weight: 700;
  }

  .contacts {
    position: absolute; right: 22px; top: 118px;
    text-align: right; font-size: 11.5px; line-height: 17px; color: var(--ink);
  }
  .contacts li { list-style: none; display: flex; justify-content: flex-end; align-items: center; gap: 6px; }
  .contacts li.email { margin-top: 10px; }
  .contacts svg { width: 10px; height: 10px; }

  .rule { position: absolute; left: 22px; right: 22px; top: 198px; height: 1px; background: var(--rule); }
  .rule__accent { position: absolute; left: 0; top: -1px; width: 155px; height: 3px; background: var(--purple); }

  .person { position: absolute; left: 22px; top: 160px; }
  .person__name { color: var(--green); font-size: 15px; font-weight: 700; }
  .person__title { color: var(--ink); font-size: 11.5px; font-weight: 700; margin-top: 1px; }
  .address {
    position: absolute; left: 22px; top: 212px;
    font-size: 12px; line-height: 16px; color: var(--ink-soft); font-style: normal;
  }
</style>
</head>
<body>
<main class="stage">
  <section class="card card--front">
    <div class="brand">
      <div class="brand__row">
        <span class="brand__dot"></span>
        <span class="brand__name">CareerPathlane</span>
      </div>
      <span class="brand__tagline">Building your next step</span>
    </div>

    <ul class="contacts">
      <li>555.201.4418
        <svg viewBox="0 0 10 10"><rect width="10" height="10" rx="1.5" fill="#8cb92b"/><path d="M2.6 2.2c.4-.3.8-.2 1 .2l.6 1c.2.3.1.6-.2.8l-.3.2c.3.7.9 1.3 1.6 1.6l.2-.3c.2-.3.5-.4.8-.2l1 .6c.4.2.5.6.2 1l-.5.6C5.5 8 2 4.5 2.1 2.7z" fill="#fff"/></svg>
      </li>
      <li>555.307.6620
        <svg viewBox="0 0 10 10"><rect width="10" height="10" rx="1.5" fill="#8cb92b"/><rect x="3" y="1.8" width="4" height="2.2" fill="#fff"/><rect x="1.8" y="4.2" width="6.4" height="2.6" rx=".5" fill="#fff"/><rect x="3" y="6.4" width="4" height="1.8" fill="#fff"/></svg>
      </li>
      <li class="email">malik@careerpathlane-demo.com
        <svg viewBox="0 0 10 10"><rect width="10" height="10" rx="1.5" fill="#8cb92b"/><rect x="1.8" y="2.8" width="6.4" height="4.4" fill="#fff"/><path d="M1.8 2.8 5 5.4 8.2 2.8" fill="none" stroke="#8cb92b" stroke-width=".8"/></svg>
      </li>
    </ul>

    <div class="person">
      <p class="person__name">Malik Darrow</p>
      <p class="person__title">Principal</p>
    </div>
    <div class="rule"><span class="rule__accent"></span></div>
    <address class="address">480 N. Harlow Street<br>Riverton, IL 60999</address>
  </section>

  <section class="card card--back">
    <div class="brand">
      <div class="brand__row">
        <span class="brand__dot"></span>
        <span class="brand__name">CareerPathlane</span>
      </div>
      <span class="brand__tagline">Building your next step</span>
    </div>
    <p class="web">www.careerpathlane-demo.com</p>
  </section>
</main>
</body>
</html>
```